Bref créative
FoodTruck Wrap design
Marlows
Need a design for a food truck trailer for a restaurant selling crawfish and bbq. The logo has an image of a crawfish but the restaurant also wants to promote bbq plate lunches. We need a design to incorporate both. Pictures of food truck attached for template, and logo
Food
lunch crowd, cajuns
Drivers side window will be closed in-no need to design around the window

```html
<!DOCTYPE html>
<html lang="en">
<head>
<meta charset="utf-8">
<title>Marlows Food Truck Wrap</title>
<link href="https://fonts.googleapis.com/css2?family=Rokkitt:ital,wght@0,700;1,700&family=Alfa+Slab+One&family=Playfair+Display:wght@700&display=swap" rel="stylesheet">
<style>
  :root {
    --backdrop: #a8a8a8;
    --band-dark: #2c1107;
    --band-mid: #4a2210;
    --band-lower: #6e3d1d;
    --band-lower-light: #8a5128;
    --stripe-red: #b3121a;
    --sauce-red: #c8141c;
    --flame-orange: #e0541d;
    --tagline-gold: #e6a93a;
    --cream: #f3e3c2;
    --white: #ffffff;
  }
  * { margin: 0; padding: 0; box-sizing: border-box; }
  html, body { width: 1200px; height: 780px; overflow: hidden; }
  body { background: var(--backdrop); position: relative; font-family: "Rokkitt", serif; }

  .wrap {
    position: absolute; left: 40px; top: 215px; width: 1120px; height: 350px;
    background: linear-gradient(180deg, var(--band-dark) 0%, var(--band-mid) 58%, var(--band-lower) 58%, var(--band-lower-light) 100%);
    overflow: hidden;
  }
  .wrap__stripe { position: absolute; left: 0; right: 0; top: 198px; height: 8px; background: var(--stripe-red); }
  .wrap__stripe--thin { top: 210px; height: 2px; opacity: .8; }

  .logo-art { position: absolute; left: 0; top: 40px; width: 300px; height: 310px; }

  .headline {
    position: absolute; left: 22px; top: 18px;
    font-style: italic; font-weight: 700; font-size: 22px; letter-spacing: .5px;
    color: var(--tagline-gold);
  }
  .brand {
    position: absolute; left: 150px; top: 60px;
    font-family: "Rokkitt", serif; font-weight: 700; font-size: 84px; line-height: 1;
    color: var(--white); display: flex; align-items: center; gap: 14px;
  }
  .brand__dot { width: 18px; height: 18px; border-radius: 50%; background: var(--white); }
  .slogan {
    position: absolute; right: 30px; top: 160px;
    font-style: italic; font-weight: 700; font-size: 30px; letter-spacing: 1px;
    color: var(--tagline-gold);
  }
  .offer-fresh {
    position: absolute; left: 300px; top: 222px;
    font-style: italic; font-weight: 700; font-size: 34px; color: var(--cream);
  }
  .offer-crawfish {
    position: absolute; left: 305px; top: 262px;
    font-family: "Playfair Display", serif; font-weight: 700; font-size: 44px; letter-spacing: 2px;
    color: var(--sauce-red); -webkit-text-stroke: 1.5px var(--white);
  }
  .offer-and {
    position: absolute; left: 580px; top: 222px;
    font-style: italic; font-weight: 700; font-size: 50px; color: var(--cream);
  }
  .offer-bbq {
    position: absolute; left: 630px; top: 218px;
    font-family: "Alfa Slab One", serif; font-size: 78px; line-height: 1; letter-spacing: 3px;
    color: var(--sauce-red); -webkit-text-stroke: 2px var(--white);
  }
</style>
</head>
<body>
  <div class="wrap">
    <div class="wrap__stripe"></div>
    <div class="wrap__stripe wrap__stripe--thin"></div>

    <svg class="logo-art" viewBox="0 0 300 310" role="img" aria-label="Illustration of a red crawfish surrounded by flames">
      <defs>
        <radialGradient id="flameGlow" cx="40%" cy="55%" r="60%">
          <stop offset="0%" stop-color="#b3121a"/>
          <stop offset="60%" stop-color="#e0541d"/>
          <stop offset="100%" stop-color="#e0541d" stop-opacity="0"/>
        </radialGradient>
      </defs>
      <ellipse cx="120" cy="170" rx="125" ry="130" fill="url(#flameGlow)"/>
    </svg>

    <p class="headline">Hitting the Streets with 20 years of Acadiana's Finest Fair</p>
    <div class="brand"><span class="brand__name">Marlows</span><span class="brand__dot"></span></div>
    <p class="slogan">Low 'n' Slow and Ready To Go</p>
    <p class="offer-fresh">Fresh &amp; Wild</p>
    <p class="offer-crawfish">CRAWFISH</p>
    <p class="offer-and">&amp;</p>
    <p class="offer-bbq">BBQ</p>
  </div>
</body>
</html>
```